Law firm website marketed direct to many individual clients

I need someone to design a very basic website for a law firm that will be very eye catching. It's going to be a single-paged, scrolling website with a small number of folds. I have uploaded a simple word document that outlines the basics of what I thought could be the layout, but I am open to suggestion on font, size, shades of color, organization, etc. etc. Essentially the website just needs to be a very efficient and visually appealing way of conveying some simple messages.

Target Market(s)

High volumes of individuals who have gotten into a car accident and then google on their phones a lawyer to hire to represent them.

Industry/Entity Type

Legal

Number of Pages Required

1 page

Font styles to use
Serif
Sans Serif

Colors
34a7d7
85cae6
0592cd

Requirements
Must have
• Must be bright and grab the users attention with color scheme and layout. The different sections should be done in such a way that they can fit entirely onto one smart phone or tablet screen.
Nice to have
• I'd like to try and see what it looks like if in the middle somewhere there is a fold that says "MEET YOUR ATTORNEYS" and includes individual photos of two attorneys, one on the left side and one on the right. And then a small bio section on them. I don't want the photos to include a square or rectangle background, I want the person in the photo to be superimposed on top of whatever pattern or background you have in the fold.
Should not have
• Do not want too much text. Anything more than 2 sentences in any single place is unacceptable.

```html
<!DOCTYPE html>
<html lang="en">
<head>
<meta charset="utf-8">
<title>Harborline Law Group</title>
<link href="https://fonts.googleapis.com/css2?family=Noto+Serif:wght@400;700&family=Amatic+SC:wght@700&display=swap" rel="stylesheet">
<style>
:root{
  --blue:#0592cd;
  --blue-mid:#34a7d7;
  --blue-light:#85cae6;
  --ink:#333333;
  --logo-ink:#444444;
  --orange:#f47b20;
  --orange-deep:#f06a14;
  --yellow:#ffd21c;
  --navy:#2f3a6b;
  --navy-btn:#4a4a78;
  --white:#ffffff;
}
*{margin:0;padding:0;box-sizing:border-box}
html,body{width:719px;height:1200px;overflow:hidden;background:var(--white)}
body{font-family:"Noto Serif",Georgia,serif;color:var(--ink);position:relative}
.site-header{position:absolute;left:0;top:0;width:719px;height:63px}
.brand{position:absolute;left:106px;top:22px;font-size:17px;font-variant:small-caps;letter-spacing:.5px;color:var(--logo-ink);font-weight:400}
.header-phone{position:absolute;left:498px;top:22px;font-size:15px;color:var(--blue);display:flex;align-items:center;gap:5px}
.icon{width:12px;height:12px;fill:none;stroke:currentColor;stroke-width:1.6}
.hero{position:absolute;left:0;top:63px;width:719px;height:288px;color:var(--white);text-align:center;overflow:hidden}
.photo{position:absolute;inset:0}
.hero .photo{background:linear-gradient(100deg,#3aa6d6 0%,#2a9bd0 45%,#1b8fc7 70%,#2ba0d4 100%)}
.hero-content{position:relative}
.hero-title{position:absolute;left:0;width:719px;top:88px;font-size:23px;font-weight:400;letter-spacing:.3px}
.hero-tag{position:absolute;left:0;width:719px;top:130px;font-size:11px}
.hero-call{position:absolute;left:0;width:719px;top:158px;font-size:23px;font-weight:400}
.btn-learn{position:absolute;left:311px;top:207px;width:96px;height:25px;background:var(--blue-light);color:var(--white);font-size:11px;line-height:25px;text-align:center}
.benefits{position:absolute;left:0;top:351px;width:719px;height:421px;text-align:center}
.benefit{position:absolute;left:0;width:719px}
.benefit h2{font-size:23px;font-weight:400;color:var(--blue);letter-spacing:.2px;line-height:28px}
.benefit p{font-size:8.5px;margin-top:2px}
.btn-call{position:absolute;width:185px;height:40px;display:flex;align-items:center;justify-content:center;gap:5px;color:var(--white);font-size:14px;font-weight:700}
.btn-call .icon{width:13px;height:13px}
.btn-call.light{left:267px;top:357px;background:var(--blue-light)}
.promise{position:absolute;left:0;top:772px;width:719px;height:304px;text-align:center;color:var(--white);overflow:hidden}
.promise .photo{background:linear-gradient(90deg,#f58a3a 0%,#f47b20 40%,#f7882c 75%,#f58e3a 100%)}
.promise-title{position:absolute;left:0;width:719px;font-family:"Amatic SC","Arial Narrow",sans-serif;font-weight:700;font-size:24px}
.promise-title.win{top:42px;color:var(--yellow)}
.promise-title.ask{top:120px;color:var(--navy)}
.promise-text{position:absolute;left:140px;width:439px;font-size:8.7px;line-height:13.5px}
.promise-text.win{top:73px;left:100px;width:519px}
.promise-text.ask{top:164px}
.btn-call.dark{left:267px;top:223px;background:var(--navy-btn)}
.site-footer{position:absolute;left:0;top:1076px;width:719px;height:124px;text-align:center}
.footer-address{position:absolute;left:0;width:719px;top:39px;font-size:9px}
.footer-phone{position:absolute;left:0;width:719px;top:56px;font-size:23px;color:var(--blue);display:flex;justify-content:center;align-items:center;gap:6px}
.footer-phone .icon{width:13px;height:13px}
.footer-legal{position:absolute;left:0;width:719px;top:98px;font-size:6.5px;color:#222}
</style>
</head>
<body>
<header class="site-header">
  <div class="brand">Harborline Law Group</div>
  <div class="header-phone">
    <svg class="icon" viewBox="0 0 24 24"><path d="M5 3h4l2 5-3 2a12 12 0 0 0 6 6l2-3 5 2v4a2 2 0 0 1-2 2A18 18 0 0 1 3 5a2 2 0 0 1 2-2z"/></svg>
    504-555- 0142
  </div>
</header>

<section class="hero">
  <div class="photo" role="img" aria-label="Photo of an injured person with an arm in a cast, tinted blue"></div>
  <div class="hero-content">
    <h1 class="hero-title">ACCIDENT? INJURED?</h1>
    <p class="hero-tag">YOUR CASE YOUR MONEY</p>
    <p class="hero-call">CALL 504-555- 0142</p>
    <div class="btn-learn">LEARN MORE</div>
  </div>
</section>

<section class="benefits">
  <div class="benefit" style="top:40px"><h2>LOW FEES</h2><p>We charge less, so you keep more.</p></div>
  <div class="benefit" style="top:116px"><h2>FREE CONSULTATION</h2><p>It’s always free to talk to us.</p></div>
  <div class="benefit" style="top:192px"><h2>GET STARTED USING ONLY YOUR PHONE</h2><p>No need to come to the office, sign up using your phone.</p></div>
  <div class="benefit" style="top:276px"><h2>SPEAK DIRECTLY TO A LAWYER</h2><p>It’s No staff screening. Talk right to a lawyer on your first call.</p></div>
  <div class="btn-call light">
    <svg class="icon" viewBox="0 0 24 24"><path d="M5 3h4l2 5-3 2a12 12 0 0 0 6 6l2-3 5 2v4a2 2 0 0 1-2 2A18 18 0 0 1 3 5a2 2 0 0 1 2-2z"/></svg>
    CALL 504-555- 0142
  </div>
</section>

<section class="promise">
  <div class="photo" role="img" aria-label="Photo of support staff wearing headsets at computers, tinted orange"></div>
  <h2 class="promise-title win">NO FEE UNLESS WE WIN</h2>
  <p class="promise-text win">We don’t get paid unless you get paid. Its as simple as that. We let our results do the talking for us.</p>
  <h2 class="promise-title ask">QUESTIONS ABOUT ANYTHING?</h2>
  <p class="promise-text ask">We&amp;re here to help. Feel free to call us at 504-555- 0142 to speak to one of our attorneys. With extensive experience in helping clients get the results that they want, our team is always just a phone call away.</p>
  <div class="btn-call dark">
    <svg class="icon" viewBox="0 0 24 24"><path d="M5 3h4l2 5-3 2a12 12 0 0 0 6 6l2-3 5 2v4a2 2 0 0 1-2 2A18 18 0 0 1 3 5a2 2 0 0 1 2-2z"/></svg>
    CALL 504-555- 0142
  </div>
</section>

<footer class="site-footer">
  <p class="footer-address">Harborline Law Group &nbsp;|&nbsp; Somewhere Office Row | New Orleans, LA 70112</p>
  <p class="footer-phone">
    <svg class="icon" viewBox="0 0 24 24"><path d="M5 3h4l2 5-3 2a12 12 0 0 0 6 6l2-3 5 2v4a2 2 0 0 1-2 2A18 18 0 0 1 3 5a2 2 0 0 1 2-2z"/></svg>
    504-555- 0142
  </p>
  <p class="footer-legal">© 2016 Company Name &nbsp;|&nbsp; All Rights Reserved</p>
</footer>
</body>
</html>
```